Ironbark & Vale Construction and Developments business cards

A business card with watermark background (construction work)

Home improvement projects
House renovations
Bathroom and kitchen renovations
House extensions
New builds and granny flats

Director Tomas Verhoeven
(Phone number)
tomas@ivkbuilds.com.au
(Instagram logo) ivk_builds

```html
<!DOCTYPE html>
<html lang="en">
<head>
<meta charset="UTF-8">
<title>Ironbark &amp; Vale – Business Cards</title>
<link rel="stylesheet" href="https://fonts.googleapis.com/css2?family=Poppins:wght@400;500;700&display=swap">
<style>
  :root {
    --page-bg: #e8e9eb;
    --brand-blue: #2d6ca6;
    --card-white: #f4f4f4;
    --ink-dark: #2f3a44;
    --rule-blue: #4a7fb5;
    --photo-warm: #e9ddd0;
    --photo-green: #c9d5c4;
  }
  * { box-sizing: border-box; margin: 0; padding: 0; }
  html, body {
    width: 1200px; height: 944px; overflow: hidden;
    background: var(--page-bg);
    font-family: "Poppins", sans-serif;
  }
  .sheet {
    width: 1200px; height: 944px;
    display: flex; flex-direction: column; align-items: center; justify-content: center;
    gap: 40px;
  }
  .card {
    position: relative;
    width: 740px; height: 422px;
    border-radius: 4px;
    box-shadow: 0 6px 18px rgba(0,0,0,.12);
    overflow: hidden;
  }
  /* Front */
  .card--front {
    background: var(--brand-blue);
    display: flex; align-items: center; justify-content: center;
  }
  .wordmark {
    display: flex; flex-direction: column; align-items: center; gap: 14px;
    color: #fff; text-align: center;
  }
  .wordmark__row { display: flex; align-items: center; gap: 14px; }
  .wordmark__square { width: 22px; height: 22px; background: currentColor; }
  .wordmark__name {
    font-weight: 700; font-size: 30px; line-height: 1.15; letter-spacing: .2px;
  }
  .wordmark__tagline {
    font-size: 17px; font-weight: 400;
    border-bottom: 1.5px solid currentColor; padding-bottom: 3px;
  }
  /* Back */
  .card--back { background: var(--card-white); }
  .photo-wash {
    position: absolute; inset: 0 0 0 32%;
    background:
      radial-gradient(ellipse at 70% 45%, var(--photo-warm) 0%, transparent 55%),
      radial-gradient(ellipse at 55% 80%, var(--photo-green) 0%, transparent 60%),
      linear-gradient(90deg, var(--card-white) 0%, #ecebe8 40%, #e6e4df 100%);
    opacity: .75;
  }
  .back-layout {
    position: relative; height: 100%;
    display: flex; align-items: center; padding: 0 40px 0 56px; gap: 28px;
  }
  .back-layout .wordmark { color: var(--brand-blue); width: 290px; gap: 10px; }
  .back-layout .wordmark__name { font-size: 22px; }
  .back-layout .wordmark__square { width: 16px; height: 16px; }
  .back-layout .wordmark__tagline { font-size: 14px; }
  .divider { width: 1.5px; height: 190px; background: var(--rule-blue); }
  .contact { color: var(--ink-dark); }
  .contact__name { color: var(--brand-blue); font-weight: 700; font-size: 30px; line-height: 1.1; }
  .contact__role { font-size: 16px; margin-bottom: 20px; }
  .contact__list { list-style: none; display: flex; flex-direction: column; gap: 8px; font-size: 16px; }
  .contact__item { display: flex; align-items: center; gap: 12px; }
  .contact__icon { width: 16px; height: 16px; flex: none; color: var(--brand-blue); }
</style>
</head>
<body>
<main class="sheet">
  <section class="card card--front" aria-label="Card front">
    <div class="wordmark">
      <div class="wordmark__row">
        <span class="wordmark__square"></span>
        <span class="wordmark__name">Ironbark &amp; Vale<br>Construction and Developments</span>
      </div>
      <span class="wordmark__tagline">Built right, start to finish!</span>
    </div>
  </section>

  <section class="card card--back" aria-label="Card back">
    <div class="photo-wash" role="img" aria-label="Faded photo of a hand passing house keys in front of a newly built home"></div>
    <div class="back-layout">
      <div class="wordmark">
        <div class="wordmark__row">
          <span class="wordmark__square"></span>
          <span class="wordmark__name">Ironbark &amp; Vale<br>Construction and Developments</span>
        </div>
        <span class="wordmark__tagline">Built right, start to finish!</span>
      </div>
      <div class="divider"></div>
      <div class="contact">
        <p class="contact__name">Tomas Verhoeven</p>
        <p class="contact__role">Managing Director</p>
        <ul class="contact__list">
          <li class="contact__item">
            <svg class="contact__icon" viewBox="0 0 24 24" fill="currentColor"><path d="M6.6 10.8a15.1 15.1 0 0 0 6.6 6.6l2.2-2.2a1 1 0 0 1 1-.25 11.4 11.4 0 0 0 3.6.57 1 1 0 0 1 1 1V20a1 1 0 0 1-1 1A17 17 0 0 1 3 4a1 1 0 0 1 1-1h3.5a1 1 0 0 1 1 1c0 1.25.2 2.45.57 3.57a1 1 0 0 1-.25 1z"/></svg>
            (013) 482-5170
          </li>
          <li class="contact__item">
            <svg class="contact__icon" viewBox="0 0 24 24" fill="currentColor"><path d="M2 5h20v14H2z" opacity=".9"/><path d="M2 5l10 8 10-8" fill="none" stroke="#f4f4f4" stroke-width="2"/></svg>
            tomas@ivkbuilds.com.au
          </li>
          <li class="contact__item">
            <svg class="contact__icon" viewBox="0 0 24 24"><circle cx="12" cy="12" r="8" fill="currentColor"/></svg>
            @ivk_builds
          </li>
        </ul>
      </div>
    </div>
  </section>
</main>
</body>
</html>
```